**Designs Wanted for High Profile Banner Ad Campaign**

Our leading Public Relations agency services some of the world's leading brands in our local market.

We now need a banner ad design to support our own growth.

We are looking to have banner ads designed that will carry a common theme to be used across the following sizes (all these sizes will need to be created):
• Vertical rectangle: 240 x 400
• Mobile leaderboard: 320 x 50
• Banner: 468 x 60
• Leaderboard: 728 x 90
• Square: 250 x 250
• Small square: 200 x 200
• Large rectangle: 336 x 280
• Inline rectangle: 300 x 250
• Skyscraper: 120 x 600
• Wide skyscraper: 160 x 600
• Half-page: 300 x 600
• Large leaderboard: 970x90
• Large mobile banner: 320 x 100
• Billboard: 970 x 250

Our primary retargeting and regular display campaign objective is to encourage marketing managers and business owners to visit our site and contact us.
See www.lumenvoicecomms.co.nz for our current look and feel. Please keep consistent colours with that site. Our two logos are attached.

This is our first digital retargeting campaign and we are open to your advice and suggestions on what will encourage click through from potential clients.

Our current thinking at the moment is that the ad could be built around these concepts:
“Reach, socialise, inspire.”
In others words – as a PR agency we help clients ‘reach’ their target market through creating content for news media.
The ‘socialise’ represents engagement through social media – in that we help develop and build their social media presence.
‘Inspire’ refers to the fact we aim to inspire their target market towards engaging with our clients.
Plus a suitable call to action– eg. Click here to meet your public relations needs today.

In terms of designs we are open to suggestion: eg. the adverts could use icons or something else that you have seen work.

We would like to see some eye catching animation, interaction or movement in the advert to.

We need the ad to be effective, eye catching, professional, modern, sophisticated (in that our target market is professional executives) and crisp, clean and uncluttered.

Time is short for us, so please send through designs as soon as possible – don’t wait until the last day!

Additional note: the existing fish image and 'stand out from the crowd' slogan on our home page are not required as part of this design. We have been looking to move towards the new slogan (“Reach, socialise, inspire.” ) and this banner ad may also serve to give us some new direction ideas as well. we do need to keep the existing logo and orange colour though.

Target Market(s)

Business to Business. Marketing and brand managers, Small, Medium and large business owners and executives.
Those with a business in the New Zealand market.

Industry/Entity Type

Marketing

Requirements
Must have
• our logo
animation or movement
orange colour/ consistency with our existing website.
our proposed slogan: “Reach, socialise, inspire.” (however we are open to seeing alternative ideas as well if you want to submit more than one concept)
call to action.
Should not have
• read note about existing fish and slogan above.

```html
<!DOCTYPE html>
<html lang="en">
<head>
<meta charset="utf-8">
<title>Lumen Voice – Reach Socialise Inspire banner set</title>
<link rel="stylesheet" href="https://fonts.googleapis.com/css2?family=Oswald:wght@400;700&family=Roboto+Condensed:ital,wght@0,700;1,400&display=swap">
<style>
:root{
  --bg:#151515;
  --orange:#e8621c;
  --white:#ffffff;
  --lime:#c4ef3f;
  --navy:#1f3a8f;
  --cyan:#2fd3e6;
  --cta-ink:#1d2f6b;
  --grey:#4a4a4a;
  --peach:#ffe3d2;
}
*{box-sizing:border-box;margin:0;padding:0}
html,body{width:1200px;height:759px;overflow:hidden;background:var(--bg)}
body{position:relative;font-family:"Oswald",sans-serif}

/* ---------- banner shell ---------- */
.ad{position:absolute;overflow:hidden;background:var(--orange)}
.ad__art{position:absolute;background:radial-gradient(circle at 45% 60%,var(--lime) 0,var(--lime) 10%,var(--grey) 32%)}
.ad__cap{position:absolute;background:var(--white);border-radius:50%}
.brand{position:absolute;display:flex;align-items:center;justify-content:center;text-align:center;
  color:var(--orange);font-family:"Oswald",sans-serif;font-weight:400;font-size:var(--fs-logo);line-height:1;letter-spacing:.04em}

/* horizontal: art left, logo cap right */
.ad--h .ad__art{left:0;top:0;bottom:0;width:var(--art);clip-path:polygon(0 0,62% 0,100% 100%,0 100%)}
.ad--h .ad__cap{top:-35%;bottom:-35%;right:calc(var(--cap) * -1);width:calc(var(--cap) * 2)}
.ad--h .brand{top:0;bottom:0;right:0;width:var(--cap);padding-left:4%}

/* vertical & box: logo cap top, art bottom */
.ad--v .ad__cap,.ad--b .ad__cap{left:-25%;right:-25%;top:calc(var(--cap) * -1);height:calc(var(--cap) * 2)}
.ad--v .brand,.ad--b .brand{top:0;left:0;right:0;height:var(--cap)}
.ad--v .ad__art,.ad--b .ad__art{left:0;right:0;bottom:0;height:var(--art);clip-path:polygon(0 40%,100% 0,100% 100%,0 100%)}
.ad--b .ad__art{background:radial-gradient(circle at 70% 55%,var(--lime) 0,var(--lime) 10%,var(--grey) 30%)}

/* ---------- copy ---------- */
.ad__copy{position:absolute;display:flex;flex-direction:column;gap:var(--gap,4px)}
.copy-main,.copy-action{display:flex;flex-direction:column;align-items:inherit;gap:var(--gap,4px)}
.slogan{font-weight:700;font-size:var(--fs-slogan);line-height:1.1;white-space:nowrap;letter-spacing:.01em}
.slogan span+span{margin-left:.35em}
.reach{color:var(--lime)}
.socialise{color:var(--white)}
.inspire{color:var(--navy)}
.ad--stack .slogan span{display:block;margin:0 0 .3em}
.ad--stack .slogan span+span{margin-left:0}
.tagline{font-family:"Roboto Condensed",sans-serif;font-style:italic;color:var(--peach);font-size:var(--fs-tag);line-height:1.35}
.cta{display:inline-block;background:var(--cyan);color:var(--cta-ink);font-weight:700;font-size:var(--fs-cta);
  line-height:1;padding:.35em .8em;border-radius:.25em;text-decoration:none;white-space:nowrap}
.url{font-family:"Roboto Condensed",sans-serif;font-weight:700;color:var(--white);font-size:var(--fs-url);white-space:nowrap}

/* ---------- individual sizes ---------- */
.billboard{left:62px;top:44px;width:594px;height:154px;--art:250px;--cap:124px;--fs-logo:28px;
  --fs-slogan:20px;--fs-tag:9.5px;--fs-cta:15px;--fs-url:8.5px;--gap:7px}
.billboard .ad__copy{left:190px;top:38px;width:270px;align-items:center;text-align:center}

.large-rect{left:687px;top:35px;width:206px;height:172px;--cap:34px;--art:66px;--fs-logo:19px;
  --fs-slogan:13.5px;--fs-tag:7px;--fs-cta:11px;--fs-url:5.8px;--gap:6px}
.large-rect .ad__copy{left:12px;top:50px;width:190px;align-items:flex-start}

.mobile-banner{left:937px;top:145px;width:197px;height:62px;--art:70px;--cap:32px;--fs-logo:8.5px;
  --fs-slogan:7px;--fs-tag:3.4px;--fs-cta:5.5px;--fs-url:3.3px;--gap:2px}
.mobile-banner .ad__copy{left:66px;top:9px;width:100px;align-items:center;text-align:center}

.skyscraper{left:62px;top:245px;width:99px;height:367px;--cap:72px;--art:100px;--fs-logo:21px;
  --fs-slogan:16px;--fs-tag:7px;--fs-cta:10px;--fs-url:5.3px;--gap:6px}
.skyscraper .ad__copy{left:7px;top:98px;width:90px;align-items:flex-start}

.inline-rect{left:224px;top:245px;width:184px;height:154px;--cap:32px;--art:66px;--fs-logo:18px;
  --fs-slogan:12px;--fs-tag:6.3px;--fs-cta:11px;--fs-url:5.3px;--gap:5px}
.inline-rect .ad__copy{left:8px;top:45px;width:170px;align-items:flex-start}

.half-page{left:472px;top:245px;width:184px;height:367px;--cap:90px;--art:120px;--fs-logo:30px;
  --fs-slogan:20px;--fs-tag:7.5px;--fs-cta:13px;--fs-url:6.6px;--gap:7px}
.half-page .ad__copy{left:38px;top:98px;width:140px;align-items:flex-start}

.wide-sky{left:716px;top:245px;width:74px;height:367px;--cap:70px;--art:95px;--fs-logo:15px;
  --fs-slogan:13px;--fs-tag:6px;--fs-cta:8.5px;--fs-url:4.1px;--gap:6px}
.wide-sky .ad__copy{left:5px;top:100px;width:66px;align-items:flex-start}

.banner{left:846px;top:245px;width:288px;height:36px;--art:55px;--cap:38px;--fs-logo:9px;
  --fs-slogan:8px;--fs-tag:4px;--fs-cta:5.5px;--fs-url:3.6px;--gap:2px}
.banner .ad__copy{left:58px;top:6px;width:185px;flex-direction:row;justify-content:space-between;align-items:center}

.mobile-lead{left:846px;top:305px;width:197px;height:30px;--art:42px;--cap:26px;--fs-logo:6.5px;
  --fs-slogan:5.5px;--fs-tag:2.8px;--fs-cta:4px;--fs-url:2.6px;--gap:1.5px}
.mobile-lead .ad__copy{left:40px;top:6px;width:128px;flex-direction:row;justify-content:space-between;align-items:center}

.square{left:846px;top:367px;width:148px;height:245px;--cap:44px;--art:80px;--fs-logo:20px;
  --fs-slogan:14px;--fs-tag:6px;--fs-cta:10px;--fs-url:4.8px;--gap:5px}
.square .ad__copy{left:48px;top:57px;width:98px;align-items:flex-start}

.small-square{left:240px;top:458px;width:154px;height:154px;--cap:28px;--art:58px;--fs-logo:15px;
  --fs-slogan:10.5px;--fs-tag:5.3px;--fs-cta:10px;--fs-url:4.6px;--gap:5px}
.small-square .ad__copy{left:7px;top:40px;width:145px;align-items:flex-start}

.mini-square{left:1040px;top:489px;width:123px;height:122px;--cap:22px;--art:46px;--fs-logo:12px;
  --fs-slogan:8.8px;--fs-tag:4.8px;--fs-cta:8.5px;--fs-url:3.8px;--gap:4px}
.mini-square .ad__copy{left:5px;top:29px;width:116px;align-items:flex-start}

.leaderboard{left:62px;top:654px;width:594px;height:55px;--art:125px;--cap:82px;--fs-logo:22px;
  --fs-slogan:20px;--fs-tag:9.5px;--fs-cta:13px;--fs-url:7px;--gap:4px}
.leaderboard .ad__copy{left:128px;top:10px;width:380px;flex-direction:row;justify-content:space-between;align-items:center}

.large-lead{left:716px;top:654px;width:447px;height:55px;--art:95px;--cap:66px;--fs-logo:17px;
  --fs-slogan:15px;--fs-tag:7.3px;--fs-cta:11px;--fs-url:6px;--gap:4px}
.large-lead .ad__copy{left:98px;top:13px;width:282px;flex-direction:row;justify-content:space-between;align-items:center}
</style>
</head>
<body>

<section class="ad ad--h billboard" aria-label="Billboard 970 x 250">
  <div class="ad__art" role="img" aria-label="Map with a laptop linked to social media icons"></div>
  <div class="ad__cap"></div><p class="brand">LUMEN<br>VOICE</p>
  <div class="ad__copy">
    <div class="copy-main"><p class="slogan"><span class="reach">REACH</span><span class="socialise">SOCIALISE</span><span class="inspire">INSPIRE</span></p>
    <p class="tagline">(MEET YOUR PUBLIC RELATIONS NEEDS TODAY)</p></div>
    <div class="copy-action"><a class="cta">CLICK HERE</a><p class="url">WWW.LUMENVOICECOMMS.CO.NZ</p></div>
  </div>
</section>

<section class="ad ad--b large-rect" aria-label="Large rectangle 336 x 280">
  <div class="ad__cap"></div><p class="brand">LUMEN VOICE</p>
  <div class="ad__art" role="img" aria-label="Map with a laptop linked to social media icons"></div>
  <div class="ad__copy">
    <div class="copy-main"><p class="slogan"><span class="reach">REACH</span><span class="socialise">SOCIALISE</span><span class="inspire">INSPIRE</span></p>
    <p class="tagline">(MEET YOUR PUBLIC RELATIONS NEEDS TODAY)</p></div>
    <div class="copy-action"><a class="cta">CLICK HERE</a><p class="url">WWW.LUMENVOICECOMMS.CO.NZ</p></div>
  </div>
</section>

<section class="ad ad--h mobile-banner" aria-label="Large mobile banner 320 x 100">
  <div class="ad__art" role="img" aria-label="Map with a laptop linked to social media icons"></div>
  <div class="ad__cap"></div><p class="brand">LUMEN<br>VOICE</p>
  <div class="ad__copy">
    <div class="copy-main"><p class="slogan"><span class="reach">REACH</span><span class="socialise">SOCIALISE</span><span class="inspire">INSPIRE</span></p>
    <p class="tagline">(MEET YOUR PUBLIC RELATIONS NEEDS TODAY)</p></div>
    <div class="copy-action"><a class="cta">CLICK HERE</a><p class="url">WWW.LUMENVOICECOMMS.CO.NZ</p></div>
  </div>
</section>

<section class="ad ad--v ad--stack skyscraper" aria-label="Skyscraper 120 x 600">
  <div class="ad__cap"></div><p class="brand">LUMEN<br>VOICE</p>
  <div class="ad__art" role="img" aria-label="Map with a laptop linked to social media icons"></div>
  <div class="ad__copy">
    <div class="copy-main"><p class="slogan"><span class="reach">REACH</span><span class="socialise">SOCIALISE</span><span class="inspire">INSPIRE</span></p>
    <p class="tagline">(MEET YOUR PUBLIC RELATIONS NEEDS TODAY)</p></div>
    <div class="copy-action"><a class="cta">CLICK HERE</a><p class="url">WWW.LUMENVOICECOMMS.CO.NZ</p></div>
  </div>
</section>

<section class="ad ad--b inline-rect" aria-label="Inline rectangle 300 x 250">
  <div class="ad__cap"></div><p class="brand">LUMEN VOICE</p>
  <div class="ad__art" role="img" aria-label="Map with a laptop linked to social media icons"></div>
  <div class="ad__copy">
    <div class="copy-main"><p class="slogan"><span class="reach">REACH</span><span class="socialise">SOCIALISE</span><span class="inspire">INSPIRE</span></p>
    <p class="tagline">(MEET YOUR PUBLIC RELATIONS NEEDS TODAY)</p></div>
    <div class="copy-action"><a class="cta">CLICK HERE</a><p class="url">WWW.LUMENVOICECOMMS.CO.NZ</p></div>
  </div>
</section>

<section class="ad ad--v ad--stack half-page" aria-label="Half-page 300 x 600">
  <div class="ad__cap"></div><p class="brand">LUMEN<br>VOICE</p>
  <div class="ad__art" role="img" aria-label="Map with a laptop linked to social media icons"></div>
  <div class="ad__copy">
    <div class="copy-main"><p class="slogan"><span class="reach">REACH</span><span class="socialise">SOCIALISE</span><span class="inspire">INSPIRE</span></p>
    <p class="tagline">(MEET YOUR PUBLIC RELATIONS<br>NEEDS TODAY)</p></div>
    <div class="copy-action"><a class="cta">CLICK HERE</a><p class="url">WWW.LUMENVOICECOMMS.CO.NZ</p></div>
  </div>
</section>

<section class="ad ad--v ad--stack wide-sky" aria-label="Wide skyscraper 160 x 600">
  <div class="ad__cap"></div><p class="brand">LUMEN<br>VOICE</p>
  <div class="ad__art" role="img" aria-label="Map with a laptop linked to social media icons"></div>
  <div class="ad__copy">
    <div class="copy-main"><p class="slogan"><span class="reach">REACH</span><span class="socialise">SOCIALISE</span><span class="inspire">INSPIRE</span></p>
    <p class="tagline">(MEET YOUR PUBLIC RELATIONS NEEDS TODAY)</p></div>
    <div class="copy-action"><a class="cta">CLICK HERE</a><p class="url">WWW.LUMENVOICECOMMS.CO.NZ</p></div>
  </div>
</section>

<section class="ad ad--h banner" aria-label="Banner 468 x 60">
  <div class="ad__art" role="img" aria-label="Map with a laptop linked to social media icons"></div>
  <div class="ad__cap"></div><p class="brand">LUMEN<br>VOICE</p>
  <div class="ad__copy">
    <div class="copy-main"><p class="slogan"><span class="reach">REACH</span><span class="socialise">SOCIALISE</span><span class="inspire">INSPIRE</span></p>
    <p class="tagline">(MEET YOUR PUBLIC RELATIONS NEEDS TODAY)</p></div>
    <div class="copy-action"><a class="cta">CLICK HERE</a><p class="url">WWW.LUMENVOICECOMMS.CO.NZ</p></div>
  </div>
</section>

<section class="ad ad--h mobile-lead" aria-label="Mobile leaderboard 320 x 50">
  <div class="ad__art" role="img" aria-label="Map with a laptop linked to social media icons"></div>
  <div class="ad__cap"></div><p class="brand">LUMEN<br>VOICE</p>
  <div class="ad__copy">
    <div class="copy-main"><p class="slogan"><span class="reach">REACH</span><span class="socialise">SOCIALISE</span><span class="inspire">INSPIRE</span></p>
    <p class="tagline">(MEET YOUR PUBLIC RELATIONS NEEDS TODAY)</p></div>
    <div class="copy-action"><a class="cta">CLICK HERE</a><p class="url">WWW.LUMENVOICECOMMS.CO.NZ</p></div>
  </div>
</section>

<section class="ad ad--v ad--stack square" aria-label="Square 250 x 250">
  <div class="ad__cap"></div><p class="brand">LUMEN<br>VOICE</p>
  <div class="ad__art" role="img" aria-label="Map with a laptop linked to social media icons"></div>
  <div class="ad__copy">
    <div class="copy-main"><p class="slogan"><span class="reach">REACH</span><span class="socialise">SOCIALISE</span><span class="inspire">INSPIRE</span></p>
    <p class="tagline">(MEET YOUR PUBLIC<br>RELATIONS NEEDS<br>TODAY)</p></div>
    <div class="copy-action"><a class="cta">CLICK HERE</a><p class="url">WWW.LUMENVOICECOMMS.CO.NZ</p></div>
  </div>
</section>

<section class="ad ad--b small-square" aria-label="Small square 200 x 200">
  <div class="ad__cap"></div><p class="brand">LUMEN VOICE</p>
  <div class="ad__art" role="img" aria-label="Map with a laptop linked to social media icons"></div>
  <div class="ad__copy">
    <div class="copy-main"><p class="slogan"><span class="reach">REACH</span><span class="socialise">SOCIALISE</span><span class="inspire">INSPIRE</span></p>
    <p class="tagline">(MEET YOUR PUBLIC RELATIONS NEEDS TODAY)</p></div>
    <div class="copy-action"><a class="cta">CLICK HERE</a><p class="url">WWW.LUMENVOICECOMMS.CO.NZ</p></div>
  </div>
</section>

<section class="ad ad--b mini-square" aria-label="Compact rectangle">
  <div class="ad__cap"></div><p class="brand">LUMEN VOICE</p>
  <div class="ad__art" role="img" aria-label="Map with a laptop linked to social media icons"></div>
  <div class="ad__copy">
    <div class="copy-main"><p class="slogan"><span class="reach">REACH</span><span class="socialise">SOCIALISE</span><span class="inspire">INSPIRE</span></p>
    <p class="tagline">(MEET YOUR PUBLIC RELATIONS<br>NEEDS TODAY)</p></div>
    <div class="copy-action"><a class="cta">CLICK HERE</a><p class="url">WWW.LUMENVOICECOMMS.CO.NZ</p></div>
  </div>
</section>

<section class="ad ad--h leaderboard" aria-label="Leaderboard 728 x 90">
  <div class="ad__art" role="img" aria-label="Map with a laptop linked to social media icons"></div>
  <div class="ad__cap"></div><p class="brand">LUMEN<br>VOICE</p>
  <div class="ad__copy">
    <div class="copy-main"><p class="slogan"><span class="reach">REACH</span><span class="socialise">SOCIALISE</span><span class="inspire">INSPIRE</span></p>
    <p class="tagline">(MEET YOUR PUBLIC RELATIONS NEEDS TODAY)</p></div>
    <div class="copy-action"><a class="cta">CLICK HERE</a><p class="url">WWW.LUMENVOICECOMMS.CO.NZ</p></div>
  </div>
</section>

<section class="ad ad--h large-lead" aria-label="Large leaderboard 970 x 90">
  <div class="ad__art" role="img" aria-label="Map with a laptop linked to social media icons"></div>
  <div class="ad__cap"></div><p class="brand">LUMEN<br>VOICE</p>
  <div class="ad__copy">
    <div class="copy-main"><p class="slogan"><span class="reach">REACH</span><span class="socialise">SOCIALISE</span><span class="inspire">INSPIRE</span></p>
    <p class="tagline">(MEET YOUR PUBLIC RELATIONS NEEDS TODAY)</p></div>
    <div class="copy-action"><a class="cta">CLICK HERE</a><p class="url">WWW.LUMENVOICECOMMS.CO.NZ</p></div>
  </div>
</section>

</body>
</html>
```